Web Site

Target Market(s)

CEOs and International Sales & Marketing Directors of International Companies who wish to expand their business reach to Dubai and the Middle East and are looking for a local professional partner to work with.

Requirements
Must have
• Creativity is key. We don't want the normal standard boxes of text and boxes of pics. Be as creative as you like.
Nice to have
• (This is only a suggestion, we welcome your creativity)
- The center of all pages could be large rotating pictures which display professional corporate men/women working in an office, images of Dubai, the UAE, skyscrapers of business towers in Dubai, ..etc.
- Images should reflect Dubai and the Arab World as a modern, fast-paced, growing modern market - Not Traditional)
Should not have
• Not so colorful, the fewer colors you use, the better.
Not Crammed or Busy
Not Traditional but modern

```html
<!DOCTYPE html>
<html lang="en">
<head>
<meta charset="utf-8">
<title>CEDAR Group</title>
<link rel="stylesheet" href="https://fonts.googleapis.com/css2?family=Questrial&family=Source+Sans+3:wght@400;600&display=swap">
<style>
  :root{
    --brand:#8c2624;
    --brand-light:#a9332f;
    --brand-dark:#7a1b1a;
    --ink:#1c1c1c;
    --text:#4a4a4a;
    --muted:#6a6a6a;
    --line:#d8d8d8;
    --band:#efefef;
    --white:#ffffff;
    --dot:#545454;
  }
  *{box-sizing:border-box;margin:0;padding:0}
  html,body{width:1200px;height:1172px;overflow:hidden;background:var(--white)}
  body{position:relative;font-family:"Source Sans 3","Myriad Pro",sans-serif;color:var(--text)}
  .topline{position:absolute;left:0;top:0;width:1200px;height:4px;background:#111}
  .utility{position:absolute;left:0;top:4px;width:1200px;height:34px;background:linear-gradient(#f4f4f4,#fbfbfb)}
  .utility-links{position:absolute;right:90px;top:9px;font-size:14px;color:var(--brand)}
  .utility-links span.sep{color:var(--brand);margin:0 10px}
  .brand{position:absolute;left:50px;top:70px;font-family:"Questrial",sans-serif;font-size:40px;color:var(--ink);letter-spacing:1px;line-height:1}
  .search{position:absolute;left:861px;top:97px;width:272px;height:33px;border:1px solid #ddd;border-radius:3px;background:#fff;box-shadow:0 2px 4px rgba(0,0,0,.12);font-size:13px;font-style:italic;color:var(--brand);padding:9px 10px}
  .search-go{position:absolute;left:1126px;top:96px;width:38px;height:38px;border-radius:50%;background:var(--brand);color:#fff;font-size:12px;text-align:center;line-height:38px}
  .stage-band{position:absolute;left:0;top:226px;width:1200px;height:407px;background:linear-gradient(90deg,#e9e9e9,#f7f7f7 50%,#ececec)}
  .nav{position:absolute;left:27px;top:173px;width:1143px;height:53px;border-radius:4px 4px 0 0;background:linear-gradient(var(--brand-light),var(--brand-dark));display:flex}
  .nav a{display:block;height:53px;line-height:53px;color:#fff;text-decoration:none;font-size:16.5px;text-align:center;border-right:1px solid rgba(255,255,255,.25)}
  .nav a:last-child{border-right:none}
  .hero{position:absolute;left:27px;top:226px;width:1145px;height:381px;background:#fff;box-shadow:0 4px 10px rgba(0,0,0,.15)}
  .hero-photo{position:absolute;left:448px;top:0;width:695px;height:379px;background:linear-gradient(120deg,#f3ece6,#d9c3b2 45%,#b0927c 70%,#eee 100%)}
  .hero-title{position:absolute;left:80px;top:63px;font-family:"Questrial",sans-serif;font-size:29px;color:var(--ink);letter-spacing:.5px}
  .hero-title em{font-style:normal;color:var(--brand)}
  .hero-sub{position:absolute;left:80px;top:103px;font-family:"Questrial",sans-serif;font-size:20px;color:var(--brand)}
  .hero-rule{position:absolute;left:80px;top:140px;width:300px;height:1px;background:linear-gradient(90deg,#e3c9c8,transparent)}
  .hero-text{position:absolute;left:80px;top:151px;width:380px;font-size:13.5px;line-height:21px;color:var(--muted)}
  .hero-btn{position:absolute;left:81px;top:231px;width:105px;height:31px;border-radius:5px;background:#111;color:#fff;font-size:14px;line-height:31px;padding-left:13px}
  .hero-btn svg{position:absolute;right:13px;top:11px}
  .dots{position:absolute;left:187px;top:308px;display:flex;gap:17px}
  .dots i{width:14px;height:14px;border-radius:50%;background:var(--dot)}
  .dots i.active{background:var(--brand)}
  .about-title{position:absolute;left:39px;top:686px;font-family:"Questrial",sans-serif;font-size:21px;color:var(--ink)}
  .about-title em{font-style:normal;color:var(--brand)}
  .about-text{position:absolute;left:39px;top:737px;width:770px;font-size:13px;line-height:20px;color:#3a3a3a}
  .about-text p+p{margin-top:20px}
  .about-photo{position:absolute;left:831px;top:722px;width:341px;height:169px;border:1px solid #ccc;border-radius:4px;background:linear-gradient(135deg,#f1f1f1,#cfd3d6 55%,#5a5a5a)}
  .footer{position:absolute;left:0;top:1070px;width:1200px;height:102px;border-top:1px solid var(--line);background:linear-gradient(#f3f3f3,#fafafa)}
  .footer-links{position:absolute;left:0;width:1200px;top:25px;text-align:center;font-size:13.5px;color:var(--muted)}
  .footer-links span.sep{margin:0 11px}
  .copyright{position:absolute;left:0;width:1200px;top:59px;text-align:center;font-size:13px;color:var(--muted)}
</style>
</head>
<body>
  <div class="topline"></div>
  <div class="utility">
    <div class="utility-links">FAQ's<span class="sep">|</span>Support<span class="sep">|</span>Contact info</div>
  </div>

  <div class="brand">CEDAR GROUP</div>

  <div class="search">SEARCH HERE..</div>
  <div class="search-go">GO</div>

  <div class="stage-band"></div>

  <nav class="nav">
    <a style="width:105px">Home</a>
    <a style="width:173px">About the Group</a>
    <a style="width:191px">Chairman's Message</a>
    <a style="width:118px">Divisions</a>
    <a style="width:178px">Group Companies</a>
    <a style="width:240px">Employment &amp; Association</a>
    <a style="width:138px">Contact us</a>
  </nav>

  <section class="hero">
    <div class="hero-photo" role="img" aria-label="Photo of a smiling group of business professionals"></div>
    <h1 class="hero-title">CEDAR GROUP <em>PUCH LINE..</em></h1>
    <div class="hero-sub">tittle line goes here</div>
    <div class="hero-rule"></div>
    <p class="hero-text">It's the simplest, cheapest and also the basic thing the search engine picks it up very easily. We at Brightline Tech provide you the best simple websites too.</p>
    <div class="hero-btn">learn more
      <svg width="7" height="10" viewBox="0 0 7 10"><path d="M1 1l4 4-4 4" stroke="#fff" stroke-width="2" fill="none"/></svg>
    </div>
    <div class="dots"><i class="active"></i><i></i><i></i><i></i><i></i></div>
  </section>

  <h2 class="about-title"><em>About</em> Cedar Group</h2>
  <div class="about-text">
    <p>CEDAR group is a Dubai-based diversified groups of companiesled by its chairman Sheikh Tariq bin Nasser Al Hadi, a member of a founding family of Dubai.<br>
    The Group has grown with Dubai, and while best known for Real Estate Investment, it is globally recognized through its involve-ment in the Legal Consultations, Media Production, General Trading, and Telecommunication Services sectors.</p>
    <p>Just as the name of Dubai has become synonymous with trade and enterprise all over the world, the name of CEDAR Group has become synonymous with dynamic growth, evidenced by its commitment to develop and grow businesses in multiple sectors</p>
  </div>
  <div class="about-photo" role="img" aria-label="Photo of a presenter at a whiteboard addressing a seated audience"></div>

  <footer class="footer">
    <div class="footer-links">Home<span class="sep">|</span>About the Group<span class="sep">|</span>Chairman's Message<span class="sep">|</span>Divisions<span class="sep">|</span>Group Companies<span class="sep">|</span>Employment &amp; Association<span class="sep">|</span>Contact us</div>
    <div class="copyright">© 2012 Company Name &nbsp;|&nbsp; All right reserved</div>
  </footer>
</body>
</html>
```